Personal Injury Lawyer Billboard

I would like a design created featuring the image of the lawyer centered in the middle of the design.
To the left of the lawyer's image it should read "INJURED?"
To the right of the lawyer's image, it should read "CALL BRUNO!"
Under Call Bruno, include the phone number 318-555-0187.
At the bottom of the design include the lawyers information "Bruno Pemberly Accident & Injury Lawyers"
PLEASE REMOVED THE BACKGROUND IMAGERY OF THE PHOTO SUBMITTED. Also, the colors for this design should match the colors shown in the logo (navy, white and relective soft gold). Please use those color combinations in ways that best stand out.

```html
<!DOCTYPE html>
<html lang="en">
<head>
<meta charset="utf-8">
<title>Bruno Pemberly Accident &amp; Injury Lawyers – Billboard</title>
<link rel="stylesheet" href="https://fonts.googleapis.com/css2?family=Bebas+Neue&family=Poppins:wght@600;700;800&display=swap">
<style>
  :root {
    --navy: #0d1a3d;
    --navy-deep: #091331;
    --navy-light: #1a2d63;
    --gold: #d2ad45;
    --white: #ffffff;
    --stage: #c4c4c4;
    --skin: #b98a6e;
    --suit: #1f2d5e;
  }
  * { box-sizing: border-box; margin: 0; padding: 0; }
  html, body { width: 1200px; height: 575px; overflow: hidden; }
  body { background: var(--stage); position: relative; }

  .billboard {
    position: absolute; left: 64px; top: 132px;
    width: 1074px; height: 312px;
    background: var(--white);
    overflow: hidden;
  }
  .lower-band {
    position: absolute; left: 0; right: 0; top: 174px; bottom: 0;
    background: radial-gradient(ellipse at 40% 20%, var(--navy-light) 0%, var(--navy) 45%, var(--navy-deep) 100%);
  }
  .headline {
    position: absolute; left: 34px; top: 24px;
    font-family: "Bebas Neue", sans-serif;
    font-size: 156px; line-height: 1;
    color: var(--gold);
    white-space: nowrap;
  }
  .firm-name {
    position: absolute; left: 35px; top: 198px;
    font-family: "Poppins", sans-serif;
    font-weight: 600; color: var(--white);
    line-height: 1.2; white-space: nowrap;
  }
  .firm-name .name { display: block; font-size: 28px; }
  .firm-name .practice { display: block; font-size: 15px; margin-top: 12px; }

  .portrait { position: absolute; inset: 0; pointer-events: none; }
  .portrait .head {
    position: absolute; left: 508px; top: 2px;
    width: 124px; height: 170px;
    border-radius: 60px 60px 40px 40px;
    background: linear-gradient(180deg, #2a211d 0%, var(--skin) 22%, #a87b61 100%);
  }
  .portrait .torso {
    position: absolute; left: 440px; top: 162px;
    width: 314px; height: 150px;
    border-radius: 70px 70px 0 0;
    background: linear-gradient(180deg, var(--suit) 0%, #18254f 100%);
  }

  .call-line {
    position: absolute; right: 34px; top: 44px;
    font-family: "Poppins", sans-serif;
    font-weight: 800; font-size: 54px; line-height: 1.1;
    color: var(--navy); white-space: nowrap;
  }
  .call-line .accent { color: var(--gold); }
  .phone {
    position: absolute; right: 34px; top: 106px;
    display: flex; align-items: center; gap: 10px;
    font-family: "Poppins", sans-serif;
    font-weight: 700; font-size: 50px; line-height: 1.1;
    color: var(--navy); white-space: nowrap;
  }
  .phone svg { width: 40px; height: 40px; flex: none; }

  .name-pill {
    position: absolute; left: 660px; top: 170px;
    width: 382px; height: 50px;
    background: var(--gold);
    border-radius: 25px;
    display: flex; align-items: center; justify-content: flex-end;
    padding-right: 18px;
    font-family: "Poppins", sans-serif;
    font-weight: 800; font-size: 28px;
    color: var(--navy); white-space: nowrap;
  }
  .practice-tag {
    position: absolute; right: 37px; top: 226px;
    text-align: right;
    font-family: "Poppins", sans-serif;
    line-height: 1.15; white-space: nowrap;
  }
  .practice-tag .lead { display: block; font-weight: 800; font-size: 29px; color: var(--gold); }
  .practice-tag .rest { display: block; font-weight: 700; font-size: 21px; color: var(--white); }
</style>
</head>
<body>
  <main class="billboard">
    <div class="lower-band" role="img" aria-label="Navy band with faint fleur-de-lis pattern"></div>

    <h1 class="headline">INJURED?</h1>

    <p class="firm-name">
      <span class="name">BRUNO PEMBERLY</span>
      <span class="practice">ACCIDENT &amp; INJURY LAWYERS</span>
    </p>

    <div class="portrait" role="img" aria-label="Cut-out photo of the lawyer in a navy suit and green tie, smiling with a raised fist">
      <div class="torso"></div>
      <div class="head"></div>
    </div>

    <p class="call-line">CALL <span class="accent">BRUNO!</span></p>

    <p class="phone">
      <svg viewBox="0 0 40 40" aria-hidden="true">
        <circle cx="20" cy="20" r="20" fill="var(--gold)"/>
        <path d="M14.5 11.5c1-.6 2-.3 2.5.6l1.6 3c.4.8.2 1.7-.5 2.2l-1.2.9c.9 2.2 2.6 4 4.8 4.9l.9-1.2c.5-.7 1.4-.9 2.2-.5l3 1.6c.9.5 1.2 1.5.6 2.5l-1 1.6c-.7 1.1-2 1.6-3.3 1.2-5.6-1.7-10-6.1-11.7-11.7-.4-1.3.1-2.6 1.2-3.3z" fill="var(--white)"/>
        <path d="M22 12.5a6 6 0 0 1 5.5 5.5M22 9a9.5 9.5 0 0 1 9 9" stroke="var(--white)" stroke-width="1.8" fill="none" stroke-linecap="round"/>
      </svg>
      <span>318-555-0187</span>
    </p>

    <div class="name-pill">BRUNO PEMBERLY</div>

    <p class="practice-tag">
      <span class="lead">ACCIDENT</span>
      <span class="rest">&amp; Injury Lawyers</span>
    </p>
  </main>
</body>
</html>
```